job vacancy cover page

I need to design a one pager for a job I'd like to apply for. The one I have done looks shit and amateur!! Wanting it to look amazing and professional (Not too professional though as they are pretty young and fun).

```html
<!DOCTYPE html>
<html lang="en">
<head>
<meta charset="utf-8">
<title>Why Me? Why Kestrel Point?</title>
<link href="https://fonts.googleapis.com/css2?family=Roboto:wght@300;400;700&display=swap" rel="stylesheet">
<style>
  :root {
    --page-bg: #e7e8ea;
    --paper: #ffffff;
    --brand-red: #c11f2f;
    --charcoal: #232323;
    --ink: #111111;
    --on-dark: #ffffff;
  }
  * { box-sizing: border-box; margin: 0; padding: 0; }
  html, body {
    width: 1096px; height: 1200px; overflow: hidden;
    background: var(--page-bg);
    font-family: "Roboto", Arial, sans-serif;
  }
  .sheet {
    position: absolute; left: 0; top: 213px;
    width: 1096px; height: 774px;
    background: var(--paper);
  }
  .why-me {
    position: absolute; left: 0; top: 25px;
    width: 1096px; height: 358px;
  }
  .why-me__band { position: absolute; inset: 0; }
  .section-title {
    position: absolute; left: 0; width: 100%;
    text-align: center; font-weight: 300; color: var(--ink);
    letter-spacing: 0.5px;
  }
  .why-me .section-title { top: 2px; font-size: 72px; line-height: 90px; }
  .why-company {
    position: absolute; left: 0; top: 383px;
    width: 1096px; height: 108px;
  }
  .why-company .section-title { top: 12px; font-size: 74px; line-height: 90px; }
  .why-company-body {
    position: absolute; left: 0; top: 491px;
    width: 1096px; height: 261px;
    background: var(--charcoal);
  }
  .column {
    position: absolute; color: var(--on-dark);
    font-size: 14px; line-height: 21px;
  }
  .column__heading {
    font-size: 26px; line-height: 33px; font-weight: 400;
    margin-bottom: 14px; height: 66px;
  }
  .column__icon { position: absolute; }
  .bullets { list-style: none; }
  .bullets li { position: relative; padding-left: 13px; }
  .bullets li::before {
    content: ""; position: absolute; left: 0; top: 8px;
    width: 5px; height: 5px; border-radius: 50%; background: var(--on-dark);
  }
  .projects p { margin: 0; }
  .projects strong { font-weight: 700; }
</style>
</head>
<body>
<main class="sheet">
  <section class="why-me">
    <svg class="why-me__band" width="1096" height="358" viewBox="0 0 1096 358" aria-hidden="true">
      <path fill="var(--brand-red)" d="M0,0 H262 C300,0 316,16 330,48 C344,82 356,94 388,94 H738 C770,94 782,82 794,52 C806,18 822,0 862,0 H1096 V358 H0 Z"/>
    </svg>
    <h1 class="section-title">Why Me?</h1>

    <div class="column" style="left:100px; top:133px; width:240px;">
      <h2 class="column__heading">If I Was<br>A Superhero</h2>
      <p>My four superpowers would be:</p>
      <ul class="bullets">
        <li>Proactiveness</li>
        <li>Creativity</li>
        <li>Pride in my work</li>
        <li>Organisational skills</li>
      </ul>
    </div>
    <svg class="column__icon" style="left:302px; top:152px;" width="34" height="52" viewBox="0 0 34 52" aria-hidden="true">
      <path fill="#fff" d="M22 0 L4 30 H15 L10 52 L32 20 H20 Z"/>
    </svg>

    <div class="column" style="left:420px; top:133px; width:266px;">
      <h2 class="column__heading" style="padding-left:4px;">Some of<br>My Success</h2>
      <ul class="bullets">
        <li>Increased client workshops by 85% across accounts.</li>
        <li>Delivered double digit revenue increase.</li>
        <li>Re-designed workshops for virtual delivery, maintaining key relationships.</li>
      </ul>
    </div>
    <svg class="column__icon" style="left:632px; top:152px;" width="38" height="50" viewBox="0 0 38 50" aria-hidden="true">
      <path fill="#fff" d="M19 0 C29 8 31 20 29 34 H9 C7 20 9 8 19 0 Z"/>
      <path fill="#fff" d="M9 24 L1 34 V40 L9 36 Z M29 24 L37 34 V40 L29 36 Z"/>
      <circle cx="19" cy="19" r="4" fill="var(--brand-red)"/>
      <circle cx="19" cy="19" r="2" fill="#fff"/>
      <path fill="#fff" d="M13 40 H25 L22 47 H16 Z"/>
    </svg>

    <div class="column" style="left:736px; top:133px; width:266px;">
      <h2 class="column__heading">Passion</h2>
      <ul class="bullets">
        <li>The development of others and / or their teams.</li>
        <li>Helping people learn and be successful in life and in their careers.</li>
        <li>Exceptional client experiences</li>
      </ul>
    </div>
    <svg class="column__icon" style="left:947px; top:148px;" width="42" height="38" viewBox="0 0 42 38" aria-hidden="true">
      <path fill="#fff" d="M21 38 L4 21 C-2 15 0 4 9 1.5 C14 0 18 2 21 6 C24 2 28 0 33 1.5 C42 4 44 15 38 21 Z"/>
    </svg>
  </section>

  <section class="why-company">
    <h1 class="section-title">Why Kestrel Point?</h1>
  </section>

  <section class="why-company-body">
    <div class="column" style="left:100px; top:26px; width:300px;">
      <h2 class="column__heading">Values that<br>Stood Out</h2>
      <ul class="bullets">
        <li>Change for the better</li>
        <li>Excellence – not mediocre</li>
        <li>Put your heart into it and give a shit</li>
        <li>Going the extra mile</li>
        <li>Take risks</li>
      </ul>
    </div>
    <div class="column" style="left:433px; top:26px; width:260px;">
      <h2 class="column__heading">What<br>You Offer</h2>
      <ul class="bullets">
        <li>Learning &amp; Developing</li>
        <li>Team</li>
        <li>Flexibility</li>
        <li>Fun</li>
      </ul>
    </div>
    <div class="column projects" style="left:742px; top:26px; width:262px;">
      <h2 class="column__heading" style="margin-bottom:11px;">Interesting<br>Projects</h2>
      <p><strong>Corvale</strong> - Leadership development and team effectiveness</p>
      <p><strong>Hartwell</strong> – Change management for true transformation</p>
      <p><strong>Brightmore</strong> – Customer centricity at Australia's most iconic department store</p>
    </div>
  </section>
</main>
</body>
</html>
```